Simple AD for Digital Publication

Total Size 5" x 5", may include boarder or not
Image Provided; crop or use as background
Incorporate Logo and text as provided

Target Market(s)

Sound Contractors / Integrators

Industry/Entity Type

Audio Video Lighting

Requirements
Must have
• Bold Look that reflects our brand. see website: tovermundic.com - cohesive text and style

```html
<!DOCTYPE html>
<html lang="en">
<head>
<meta charset="utf-8">
<title>Tovermundic Co – Become a Dealer</title>
<link rel="stylesheet" href="https://fonts.googleapis.com/css2?family=Aldrich&family=Roboto+Condensed:wght@700&family=Roboto:wght@700&display=swap">
<style>
  :root {
    --brand-red: #ab0000;
    --deep-red: #a30000;
    --ink-grey: #4a4a4a;
    --paper: #ffffff;
  }
  html, body {
    margin: 0;
    padding: 0;
    width: 1200px;
    height: 1200px;
    overflow: hidden;
    background: var(--paper);
  }
  .ad {
    position: relative;
    width: 1200px;
    height: 1200px;
    background: var(--paper);
    overflow: hidden;
    font-family: "Aldrich", sans-serif;
  }
  .ad__band {
    position: absolute;
    left: 716px;
    top: 0;
    width: 484px;
    height: 1200px;
    background: var(--brand-red);
  }
  .ad__hero {
    position: absolute;
    left: 0;
    top: 0;
    width: 1200px;
    height: 1200px;
  }
  .brand {
    position: absolute;
    left: 74px;
    top: 76px;
    display: flex;
    align-items: center;
    gap: 14px;
  }
  .brand__mark {
    width: 58px;
    height: 58px;
    background: var(--brand-red);
  }
  .brand__text {
    display: flex;
    flex-direction: column;
  }
  .brand__name {
    font-family: "Roboto Condensed", sans-serif;
    font-weight: 700;
    font-size: 46px;
    line-height: 1;
    color: var(--brand-red);
    letter-spacing: -0.5px;
  }
  .brand__tagline {
    margin-top: 2px;
    font-family: "Roboto", sans-serif;
    font-weight: 700;
    font-size: 17px;
    line-height: 1.1;
    color: var(--ink-grey);
  }
  .headline {
    position: absolute;
    left: 62px;
    top: 904px;
    margin: 0;
    font-weight: 400;
    font-size: 33px;
    line-height: 44px;
    color: var(--brand-red);
  }
  .cta {
    position: absolute;
    left: 58px;
    top: 1065px;
    display: flex;
    align-items: center;
    gap: 11px;
  }
  .cta__label {
    font-size: 33px;
    color: var(--brand-red);
  }
  .cta__button {
    display: inline-flex;
    align-items: center;
    justify-content: center;
    width: 183px;
    height: 51px;
    border-radius: 26px;
    background: linear-gradient(#c81010, var(--deep-red));
    color: var(--paper);
    font-size: 29px;
    text-decoration: none;
  }
  .site-url {
    position: absolute;
    left: 716px;
    width: 484px;
    top: 1110px;
    margin: 0;
    text-align: center;
    font-size: 34px;
    line-height: 1;
    color: var(--paper);
    letter-spacing: 1px;
  }
</style>
</head>
<body>
<main class="ad">
  <div class="ad__band"></div>

  <svg class="ad__hero" viewBox="0 0 1200 1200" xmlns="http://www.w3.org/2000/svg">
    <defs>
      <linearGradient id="stage-photo-tones" x1="0" y1="0" x2="0" y2="1">
        <stop offset="0%" stop-color="#3e3a48"/>
        <stop offset="18%" stop-color="#6e5336"/>
        <stop offset="30%" stop-color="#5d5a2e"/>
        <stop offset="42%" stop-color="#3f6b2c"/>
        <stop offset="52%" stop-color="#5f7b34"/>
        <stop offset="60%" stop-color="#4a6a2c"/>
        <stop offset="66%" stop-color="#6a5a4e"/>
        <stop offset="74%" stop-color="#3a3438"/>
        <stop offset="84%" stop-color="#8a7f8c"/>
        <stop offset="100%" stop-color="#a79ca6"/>
      </linearGradient>
    </defs>
    <circle cx="708" cy="558" r="398" fill="var(--brand-red)"/>
    <circle cx="708" cy="558" r="384" fill="var(--paper)"/>
    <circle cx="708" cy="558" r="370" fill="url(#stage-photo-tones)" role="img"
            aria-label="Photo: stage floor pocket with cables beside a lit pine garland, auditorium seats behind"/>
  </svg>

  <header class="brand">
    <span class="brand__mark"></span>
    <div class="brand__text">
      <span class="brand__name">TOVERMUNDIC CO</span>
      <span class="brand__tagline">Stage Pocket Systems Connectivity</span>
    </div>
  </header>

  <h1 class="headline">Protect and Conceal<br>High and Low Voltage<br>Connectivity</h1>

  <div class="cta">
    <span class="cta__label">Become a Dealer</span>
    <a class="cta__button" href="#">click here</a>
  </div>

  <p class="site-url">www.tovermundic.com</p>
</main>
</body>
</html>
```